Brightmoor Card Company Business Cards

We are a trading card store with Zorblix, sports and other TCG cards, we need a business card design that encompasses a clean cut, modern style with a retro flare. website is brightmoorcardco.com for reference. Can utilize a comic book era feel or a more modern outdoor feel to utilize the "Pacific Northwest" elements of tress, mountains, etc.

Industry/Entity Type

Trading cards and collectibles

Contact Information for Business Card

business name, email address, phone number, name, owner job title

Font styles to use
Sans Serif

```html
<!DOCTYPE html>
<html lang="en">
<head>
<meta charset="utf-8">
<title>Brightmoor Card Company – Business Cards</title>
<link rel="stylesheet" href="https://fonts.googleapis.com/css2?family=Montserrat:wght@400;500;600&display=swap">
<style>
  :root {
    --backdrop: #e7e5e1;
    --card: #ffffff;
    --cyan: #17b6dc;
    --slate: #6d6e70;
    --ink: #1c1c1c;
  }
  * { margin: 0; padding: 0; box-sizing: border-box; }
  html, body { width: 900px; height: 1200px; overflow: hidden; }
  body {
    position: relative;
    background: var(--backdrop);
    font-family: "Montserrat", Arial, sans-serif;
    color: var(--ink);
  }
  .card {
    position: absolute;
    background: var(--card);
    border-radius: 22px;
    overflow: hidden;
    box-shadow: 0 6px 14px rgba(0,0,0,0.18);
  }
  .card--front { left: 80px; top: 130px; width: 742px; height: 442px; }
  .card--back  { left: 78px; top: 638px; width: 744px; height: 440px; }
  .card__band {
    position: absolute; left: 0; bottom: 0; width: 100%; height: 21px; display: block;
  }
  .band-cyan { fill: var(--cyan); }
  .band-slate { fill: var(--slate); }

  .brand {
    position: absolute;
    display: flex; align-items: center;
    color: var(--slate); font-weight: 600; text-transform: uppercase;
  }
  .brand__mark { background: var(--cyan); flex: none; }
  .brand__name { line-height: 1.15; }

  .card--front .brand { left: 118px; top: 176px; width: 200px; gap: 12px; }
  .card--front .brand__mark { width: 22px; height: 22px; }
  .card--front .brand__name { font-size: 19px; letter-spacing: 0.5px; }

  .card--back .brand { left: 215px; top: 168px; width: 330px; gap: 18px; }
  .card--back .brand__mark { width: 34px; height: 34px; }
  .card--back .brand__name { font-size: 30px; letter-spacing: 0.8px; }

  .contact {
    position: absolute; left: 335px; top: 153px;
    border-left: 2px solid var(--cyan);
    padding-left: 15px; height: 182px;
  }
  .contact__name { color: var(--cyan); font-size: 27px; font-weight: 500; line-height: 1; margin-top: 0; }
  .contact__title { font-size: 16px; margin-top: 6px; }
  .contact__address { font-size: 16px; line-height: 19px; margin-top: 12px; font-style: normal; }
  .contact__list { list-style: none; margin-top: 13px; }
  .contact__item { display: flex; align-items: center; gap: 11px; font-size: 16px; height: 25px; }
  .contact__item + .contact__item { margin-top: 0; }
  .contact__item--phone { margin-bottom: 4px; }
  .icon { width: 16px; height: 16px; fill: var(--cyan); flex: none; }
</style>
</head>
<body>

<section class="card card--front" aria-label="Business card front">
  <div class="brand">
    <span class="brand__mark"></span>
    <span class="brand__name">Brightmoor Card Company</span>
  </div>

  <div class="contact">
    <p class="contact__name">Dana Whitfield</p>
    <p class="contact__title">Owner</p>
    <address class="contact__address">2840 Cedar Ridge Rd Suite<br>210 Lakewood, Ohio 44107</address>
    <ul class="contact__list">
      <li class="contact__item contact__item--phone">
        <svg class="icon" viewBox="0 0 16 16"><path d="M3.2 1.2l2.2 2.6-1.2 1.6c.9 2 2.4 3.5 4.4 4.4l1.6-1.2 2.6 2.2-1 2.4C6.6 13.2 2.8 9.4 1 4.2z"/></svg>
        06-24681357
      </li>
      <li class="contact__item">
        <svg class="icon" viewBox="0 0 16 16"><path d="M1 3h14v1.2L8 9 1 4.2zM1 5.8l7 4.8 7-4.8V13H1z"/></svg>
        info@brightmoorcardcompany.com
      </li>
      <li class="contact__item">
        <svg class="icon" viewBox="0 0 16 16"><circle cx="8" cy="8" r="7"/><path d="M1 8h14M8 1c-2.5 2.5-2.5 11.5 0 14M8 1c2.5 2.5 2.5 11.5 0 14" stroke="#fff" stroke-width="1" fill="none"/></svg>
        www.brightmoorcardcompany.com
      </li>
    </ul>
  </div>

  <svg class="card__band" viewBox="0 0 742 21" preserveAspectRatio="none">
    <polygon class="band-cyan" points="0,0 350,0 335,21 0,21"/>
    <polygon class="band-slate" points="355,0 742,0 742,21 340,21"/>
  </svg>
</section>

<section class="card card--back" aria-label="Business card back">
  <div class="brand">
    <span class="brand__mark"></span>
    <span class="brand__name">Brightmoor Card Company</span>
  </div>

  <svg class="card__band" viewBox="0 0 744 21" preserveAspectRatio="none">
    <polygon class="band-cyan" points="0,0 350,0 335,21 0,21"/>
    <polygon class="band-slate" points="355,0 744,0 744,21 340,21"/>
  </svg>
</section>

</body>
</html>
```